Flowy subpage design wanted for a modern tax/accounting firm in Switzerland

--- Introduction ---
We are a tax and accounting firm in Switzerland. We provide services for expats living in Switzerland, our service is quite exclusive and modern (digital).

We just relaunched our website www.fiscorana.ch and are happy with the design, so the desired subpage (more details below) should of course fit in.

--- Main brief ---
Please see Word File attached. The page has to include the whole text (11 chapters). A very intuitive, flowy design on only one subpage (not one page per chapter) is a MUST. Also, it is key that the design is supporting the content of the individual chapters, so it would be advantageous if you'd have a good unterstanding of the text attached.

--- Further information ---
A similar example would be this one: https://www2.brennick.com/ch/en/pages/tax/articles/living-working-switzerland.html

This one is similar in what concerns the content, but NOT what we are looking for designwise. It is very simple and looks "thrown together", just not aesthetically pleasing in our opinion.

--- Final thoughts ---
- If you blow our minds with your design, we will certainly have future work for you.
- Our clients are between 20-50 years old, well educated, high income / high wealth, English speaking and living in Switzerland.
- CI/CD information:
Fonts
Montserrat regular / medium italic / bold
Colors
White #ffffffff
Darkblue #0a2b46
Darkblue 25% #b5bfc8
Darkblue 50% #8595a4
Greenblue #0d4261

We are looking forward to your designs!
Updates

Thank you very much for the submitted designs and your efforts. Unfortunately, none of the designs meet our expectations so far. Please note the following: - Designs that do not take CI into account will not be looked at more closely. - We have received many simple designs with very simple structure and accordion elements. But more important than the simple structure is an eye-catching design! Make it flowy and beautiful - We don't want pictures of Swiss vehicles, passes or other pictures that don't actively support the text. If you can make an illustration that really fits the context, fine, otherwise better leave it without. Thank you

Target Market(s)

Expats living in Switzerland. High income earners / high net worth individuals

Industry/Entity Type

tax/accounting

Number of Pages Required

1 page

Font styles to use
Other font styles liked:
• Montserrat

Colors
0054AA
0677BA
7BADD7
CADEEF
E8F1F8

Requirements
Must have
• based on general website design
Nice to have
• intuitive, flowy, attractive representation of much text
Should not have
• basic copy/paste of the text in sections :)

```html
<!DOCTYPE html>
<html lang="en">
<head>
<meta charset="utf-8">
<title>Fiscorana Advisory – Living &amp; Working in Switzerland</title>
<link href="https://fonts.googleapis.com/css2?family=Montserrat:ital,wght@0,400;0,500;0,600;0,700;1,500&display=swap" rel="stylesheet">
<style>
:root{
  --navy:#0a2b46;
  --navy-deep:#003142;
  --greenblue:#0d4261;
  --blue:#003e65;
  --navy-25:#b5bfc8;
  --navy-50:#8595a4;
  --mist:#e3e7eb;
  --paper:#ffffff;
  --canvas:#f5f6f7;
  --ink:#5b6b7a;
  --line:#d5dbe1;
}
*{margin:0;padding:0;box-sizing:border-box}
html,body{width:1200px;height:3458px;overflow:hidden}
body{background:var(--canvas);font-family:"Montserrat",sans-serif;color:var(--ink);position:relative}
.abs{position:absolute}

/* brand board */
.brand-mark{display:flex;align-items:center;gap:10px;color:var(--navy)}
.brand-mark .dot{width:38px;height:38px;border-radius:50%;background:var(--navy);flex:none}
.brand-mark .name{font-weight:600;font-size:19px;line-height:1.1;letter-spacing:.04em;text-transform:uppercase}
.board-divider{width:1px;background:#c9d0d6}
.board-label{font-size:21px;font-weight:500;color:var(--greenblue)}
.board-text{font-size:18px;color:#6e7a86;line-height:23px}
.swatch{width:37px;height:37px;border-radius:50%}
.swatch-code{font-size:9px;color:#6e7a86}

/* page column */
.page{background:var(--paper);overflow:hidden}
.preview{background:var(--paper);overflow:hidden;box-shadow:0 6px 24px rgba(10,43,70,.18)}
.preview .inner{width:503px;transform-origin:0 0;position:relative;height:400px}

.nav{position:absolute;left:0;top:0;width:503px;height:30px;background:#fff}
.nav .logo{position:absolute;left:67px;top:7px;display:flex;align-items:center;gap:4px;color:var(--navy)}
.nav .logo .dot{width:15px;height:15px;border-radius:50%;background:var(--navy)}
.nav .logo .name{font-size:6.5px;font-weight:600;line-height:7px;text-transform:uppercase;letter-spacing:.03em}
.nav .link{position:absolute;top:12px;font-size:5px;color:var(--navy-50)}
.nav .link.active{color:var(--navy);font-weight:600}
.nav .cta{position:absolute;left:452px;top:9px;width:47px;height:14px;background:var(--navy);color:#fff;font-size:5px;display:flex;align-items:center;justify-content:center;gap:3px}
.nav .cta i{width:4px;height:5px;border:1px solid #fff;display:block}

.hero{position:absolute;left:0;top:29px;width:503px;height:160px;background:linear-gradient(100deg,#c3cfdd 0%,#d5dde7 55%,#e3e8ee 100%);overflow:hidden}
.hero .photo{position:absolute;left:268px;top:5px;width:215px;height:127px;background:linear-gradient(160deg,#dfe6ee 0%,#a9b9ca 55%,#7d91a7 100%);clip-path:polygon(40% 100%,58% 10%,75% 0,100% 18%,100% 100%)}
.hero h1{position:absolute;left:67px;top:52px;font-size:16.5px;font-weight:400;color:var(--greenblue);line-height:19px}
.hero h1 b{font-weight:600}
.hero svg{position:absolute;left:0;top:0}

.chapters .c{position:absolute;font-size:4.8px;color:var(--navy-50);white-space:nowrap}
.chapters .c.on{color:var(--navy);font-weight:600}

h2.sec{font-size:12.5px;font-weight:400;color:var(--greenblue);white-space:nowrap}
h2.sec b{font-weight:600}
.small{font-size:5px;line-height:8px;color:var(--ink)}
.small b{color:var(--navy)}
.small a{color:var(--blue);text-decoration:underline}
.small ul{padding-left:7px}
.small li{margin:0}
.light{color:#dbe3ea}

.frame{border:1px solid var(--navy-50)}
.frame.on-dark{border-color:#b5bfc8}
.card{background:#fff}
.card.dark{background:var(--navy)}
.card h3{font-size:8px;font-weight:500;color:var(--greenblue);white-space:nowrap}
.card h3 b{font-weight:600}
.card.dark h3{color:#fff}

.acc{position:absolute;height:14px;border-bottom:1px solid var(--line);font-size:5px;color:var(--greenblue);display:flex;align-items:center;padding-left:6px}
.acc::after{content:"";position:absolute;right:7px;top:4px;width:3px;height:3px;border-right:1px solid currentColor;border-bottom:1px solid currentColor;transform:rotate(45deg)}
.acc.open{background:var(--navy);color:#fff;border:none}
.acc.open::after{transform:rotate(-135deg);top:6px}
.acc.boxed{border:1px solid #56708a;color:#dbe3ea;background:transparent}
.acc.white{background:#fff;color:var(--navy);border:none}
.acc.white::after{transform:rotate(-135deg);top:6px}
.acc.dark-line{border-bottom-color:#3a5975;color:#dbe3ea}

.footer{background:var(--navy);color:#cfd8e0}
.footer .col-title{font-size:5px;font-weight:700;color:#fff;text-transform:uppercase}
.footer .tiny{font-size:4.6px;line-height:7.5px;color:#b5bfc8}
</style>
</head>
<body>

<!-- brand board -->
<div class="abs brand-mark" style="left:277px;top:112px">
  <span class="dot"></span>
  <span class="name">Fiscorana<br>Advisory</span>
</div>
<div class="abs board-divider" style="left:524px;top:91px;height:83px"></div>
<div class="abs board-label" style="left:583px;top:90px">Fonts:</div>
<div class="abs board-text" style="left:583px;top:132px">Montserrat<br>Font</div>
<div class="abs board-divider" style="left:742px;top:91px;height:83px"></div>
<div class="abs board-label" style="left:801px;top:90px">Colors:</div>
<div class="abs swatch" style="left:803px;top:123px;background:#003142"></div>
<div class="abs swatch" style="left:851px;top:123px;background:#003e65"></div>
<div class="abs swatch" style="left:897px;top:123px;background:#e3e3eb"></div>
<div class="abs swatch-code" style="left:803px;top:167px">#003142</div>
<div class="abs swatch-code" style="left:851px;top:167px">#003e65</div>
<div class="abs swatch-code" style="left:897px;top:167px">#e3e3eb</div>

<!-- desktop preview, flat -->
<div class="abs preview" style="left:469px;top:275px;width:585px;height:331px">
  <div class="inner" style="transform:scale(1.163)">
    <div class="hero"><div class="photo" role="img" aria-label="Glass office tower seen from below"></div>
      <h1>Living &amp; Working<br><b>in Switzerland</b></h1>
      <svg width="503" height="160" viewBox="0 0 503 160"><polygon points="0,152 503,90 503,160 0,160" fill="#fff"/><polygon points="250,128 503,86 503,148" fill="#0a2b46"/></svg>
    </div>
    <div class="nav"><div class="logo"><span class="dot"></span><span class="name">Fiscorana<br>Advisory</span></div>
      <span class="link" style="left:237px">Home</span><span class="link" style="left:264px">Tax returns</span><span class="link active" style="left:302px">More services ▾</span><span class="link" style="left:351px">Swiss tax guide</span><span class="link" style="left:400px">About us</span><span class="cta"><i></i>Calculate</span></div>
    <div class="chapters">
      <span class="c on" style="left:67px;top:196px">1. Life in Switzerland</span><span class="c" style="left:147px;top:196px">2. CH – A brief overview</span><span class="c" style="left:235px;top:196px">3. Immigration in CH</span><span class="c" style="left:315px;top:196px">4. Labor law in CH</span><span class="c" style="left:390px;top:196px">5. Double taxation</span>
      <span class="c" style="left:67px;top:214px">6. Indirect taxes in CH</span><span class="c" style="left:147px;top:214px">7. Other federal taxes</span><span class="c" style="left:235px;top:214px">8. Rent &amp; buy in CH</span><span class="c" style="left:315px;top:214px">9. Childcare in CH</span><span class="c" style="left:390px;top:214px">10. Public transport</span>
      <span class="c" style="left:67px;top:232px">11. Recreation</span>
    </div>
  </div>
</div>

<!-- laptop preview, flat -->
<div class="abs preview" style="left:161px;top:496px;width:382px;height:248px">
  <div class="inner" style="transform:scale(.76)">
    <div class="hero"><div class="photo" role="img" aria-label="Glass office tower seen from below"></div>
      <h1>Living &amp; Working<br><b>in Switzerland</b></h1>
      <svg width="503" height="160" viewBox="0 0 503 160"><polygon points="0,152 503,90 503,160 0,160" fill="#fff"/><polygon points="250,128 503,86 503,148" fill="#0a2b46"/></svg>
    </div>
    <div class="nav"><div class="logo"><span class="dot"></span><span class="name">Fiscorana<br>Advisory</span></div>
      <span class="link" style="left:237px">Home</span><span class="link" style="left:264px">Tax returns</span><span class="link active" style="left:302px">More services ▾</span><span class="link" style="left:351px">Swiss tax guide</span><span class="link" style="left:400px">About us</span><span class="cta"><i></i>Calculate</span></div>
    <div class="chapters">
      <span class="c on" style="left:67px;top:196px">1. Life in Switzerland</span><span class="c" style="left:147px;top:196px">2. CH – A brief overview</span><span class="c" style="left:235px;top:196px">3. Immigration in CH</span><span class="c" style="left:315px;top:196px">4. Labor law in CH</span><span class="c" style="left:390px;top:196px">5. Double taxation</span>
      <span class="c" style="left:67px;top:214px">6. Indirect taxes in CH</span><span class="c" style="left:147px;top:214px">7. Other federal taxes</span><span class="c" style="left:235px;top:214px">8. Rent &amp; buy in CH</span><span class="c" style="left:315px;top:214px">9. Childcare in CH</span><span class="c" style="left:390px;top:214px">10. Public transport</span>
      <span class="c" style="left:67px;top:232px">11. Recreation</span>
    </div>
  </div>
</div>

<!-- full subpage -->
<div class="abs page" style="left:349px;top:825px;width:503px;height:2538px">

  <div class="hero" style="height:155px"><div class="photo" role="img" aria-label="Glass office tower seen from below"></div>
    <h1>Living &amp; Working<br><b>in Switzerland</b></h1>
    <svg width="503" height="160" viewBox="0 0 503 160"><polygon points="0,152 503,92 503,160 0,160" fill="#fff"/><polygon points="250,128 503,88 503,150" fill="#0a2b46"/></svg>
  </div>
  <div class="nav"><div class="logo"><span class="dot"></span><span class="name">Fiscorana<br>Advisory</span></div>
    <span class="link" style="left:237px">Home</span><span class="link" style="left:264px">Tax returns</span><span class="link active" style="left:302px">More services ▾</span><span class="link" style="left:351px">Swiss tax guide</span><span class="link" style="left:400px">About us</span><span class="cta"><i></i>Calculate</span></div>

  <div class="chapters">
    <span class="c on" style="left:67px;top:222px">1. Life in Switzerland</span><span class="c" style="left:147px;top:222px">2. CH – A brief overview</span><span class="c" style="left:235px;top:222px">3. Immigration in CH</span><span class="c" style="left:315px;top:222px">4. Labor law in CH</span><span class="c" style="left:390px;top:222px">5. Double taxation</span>
    <span class="c" style="left:67px;top:240px">6. Indirect taxes in CH</span><span class="c" style="left:147px;top:240px">7. Other federal taxes</span><span class="c" style="left:235px;top:240px">8. Rent &amp; buy in CH</span><span class="c" style="left:315px;top:240px">9. Childcare in CH</span><span class="c" style="left:390px;top:240px">10. Public transport</span>
    <span class="c" style="left:67px;top:258px">11. Recreation</span>
  </div>

  <h2 class="sec abs" style="left:0;width:503px;text-align:center;top:293px">1.Life <b>in Switzerland</b></h2>
  <p class="small abs" style="left:100px;width:303px;top:317px;text-align:center">To give you a small impression of what to expect when living in Switzerland, we have put together some topics for you to make your new start in Switzerland as pleasant as possible.</p>

  <!-- General -->
  <div class="abs frame" style="left:60px;top:353px;width:125px;height:295px"></div>
  <div class="abs" role="img" aria-label="Aerial view of pedestrians on a lakeside promenade" style="left:67px;top:361px;width:118px;height:293px;background:linear-gradient(90deg,#4c6478 0%,#8a9aa6 45%,#6f7f8c 100%)"></div>
  <div class="abs card" style="left:185px;top:376px;width:260px;height:258px">
    <h3 class="abs" style="left:18px;top:22px">General</h3>
    <div class="acc" style="left:18px;top:40px;width:234px">4 official languages</div>
    <div class="acc open" style="left:18px;top:59px;width:234px">Currency and banking</div>
    <div class="small abs" style="left:24px;top:80px;width:222px">
      The national currency in Switzerland is the Swiss franc (CHF). 1 Swiss franc (Franken) is equal to 100 centimes (Rappen).<br>
      The banknotes are available in the following amounts: 10, 20, 50, 100, 200, 1000.<br>
      For coins, there are the following denominations:
      <ul><li><b>CHF 1, 2, 5</b></li><li>5, 10, 20, 50 centimes</li></ul>
      Current accounts can be opened at any major bank, Swiss Postbank, cantonal or private banks. The largest national banks offer services in English.
    </div>
    <div class="acc" style="left:18px;top:163px;width:234px">Public holidays</div>
    <div class="acc" style="left:18px;top:183px;width:234px">Usual business and store opening hours</div>
    <div class="acc" style="left:18px;top:203px;width:234px">Electricity and water</div>
    <div class="acc" style="left:18px;top:223px;width:234px">Telephone and television</div>
  </div>

  <!-- Living: dark band -->
  <div class="abs" style="left:0;top:687px;width:503px;height:300px;background:var(--navy)"></div>
  <svg class="abs" style="left:0;top:940px" width="503" height="60" viewBox="0 0 503 60">
    <rect x="0" y="0" width="503" height="60" fill="#e3e7eb"/>
    <polygon points="0,0 503,0 503,8 0,58" fill="#0a2b46"/>
    <polygon points="0,10 180,38 0,58" fill="#8595a4"/>
  </svg>
  <div class="abs frame on-dark" style="left:261px;top:715px;width:181px;height:211px"></div>
  <div class="abs" role="img" aria-label="Lakeside town with a historic building and moored boats" style="left:256px;top:721px;width:180px;height:211px;background:linear-gradient(180deg,#9ec3df 0%,#c9b89b 45%,#5d87a6 75%,#3f6784 100%)"></div>
  <div class="abs card dark" style="left:54px;top:742px;width:264px;height:172px;background:#0c3050">
    <h3 class="abs" style="left:14px;top:17px;font-weight:400">Living <b>in Switzerland</b></h3>
    <div class="acc boxed" style="left:14px;top:33px;width:232px">Rent</div>
    <div class="acc white" style="left:14px;top:54px;width:232px">Buy</div>
    <div class="small abs light" style="left:20px;top:76px;width:222px">
      Under certain conditions, it is also possible for non-Swiss nationals to purchase residential property in Switzerland.<br>
      A down payment of <b style="color:#fff">20%</b> of the purchase price must be made from equity; a maximum mortgage of <b style="color:#fff">80%</b> of the purchase price can be taken out.<br>
      The purchase of a property changes the tax situation of the buyer, as the residential property is henceforth included in the assets and is therefore subject to wealth tax (which varies from canton to canton). It is advisable to consult with a tax expert before purchasing a property.
    </div>
  </div>

  <!-- Education: grey band -->
  <div class="abs" style="left:0;top:998px;width:503px;height:367px;background:var(--mist)"></div>
  <div class="abs frame" style="left:60px;top:1033px;width:184px;height:301px"></div>
  <div class="abs" role="img" aria-label="Lecturer speaking to a seated audience in a bright hall" style="left:67px;top:1039px;width:177px;height:295px;background:linear-gradient(100deg,#3e5568 0%,#aab7c2 45%,#dfe5ea 70%,#7d8d9b 100%)"></div>
  <div class="abs card" style="left:185px;top:1059px;width:278px;height:262px">
    <h3 class="abs" style="left:17px;top:21px;font-weight:400">The education <b>system in Switzerland</b></h3>
    <div class="small abs" style="left:17px;top:38px;width:248px">
      In Switzerland, there are both public and private schools. The public schools are financed by the cantons and attendance at such a school is free of charge.<br>
      Compulsory kindergarten or schooling begins at the age of 4. A minimum of 11 years of schooling is compulsory.<br>
      Public educational institutions are classified as follows:
      <ul><li>Kindergarten: age 4–6 years (compulsory in most cantons)</li><li>Elementary school: ages 6–12, grades 1–6, mandatory</li><li>Secondary school: ages 12–15, compulsory, leads to completion of compulsory education</li><li>After secondary school: upper secondary schools for preparation for higher education (e.g. university) or training centres for trainees</li></ul>
      Anyone wishing to enrol their child in the Swiss public school system must contact the cantonal education authority and provide the following proof:
      <ul><li>Residence permit for Switzerland</li><li>Health and accident insurance for the child</li></ul>
      If a foreign child is between the ages of 12 and 15, he or she must pass an entrance exam before enrolling in a public school, which tests, among other things, sufficient proficiency in the language of instruction.<br>
      Enrolling the child in a private school is also possible. However, depending on the school, waiting times for a free place can be several years.
    </div>
  </div>

  <!-- Healthcare: white band -->
  <div class="abs frame" style="left:261px;top:1396px;width:181px;height:281px"></div>
  <div class="abs" role="img" aria-label="Medical staff in white coats walking down a bright corridor" style="left:256px;top:1401px;width:180px;height:275px;background:linear-gradient(180deg,#dce4ec 0%,#a9bccd 50%,#6f8aa3 100%)"></div>
  <div class="abs card" style="left:54px;top:1421px;width:264px;height:256px">
    <h3 class="abs" style="left:13px;top:17px;font-weight:400">The healthcare <b>system in Switzerland</b></h3>
    <div class="small abs" style="left:13px;top:36px;width:240px">
      The healthcare system in Switzerland is one of the best in the world. Even in less densely populated regions the density of hospitals and doctors' offices is high, so that medical care is always timely ensured.<br>
      The federal government sets the financial framework within which health insurers may offer their premiums. The federal government must also give its prior consent to premium increases and can also reject them.<br>
      The cantons and local communities are responsible for regulating hospitals. This means that it is determined at the cantonal level which hospital provides which services and how high the wages of doctors and nursing staff are.<br>
      Compulsory health insurance applies in Switzerland. This means that everyone who lives here must have health insurance. The health insurance companies are private companies, but they are only allowed to operate within the legal framework set by the federal government.<br>
      The companies are obliged to include every citizen in the so-called basic insurance, without a prior health check. Insured persons can add additional services that go beyond basic medical care to their health insurance plan at an additional cost, if they wish.<br>
      <a>Every citizen is free to choose an insurer.</a> The amount of the insurance premiums that are paid monthly differs in part very much from insurer to insurer. Therefore it is advisable to compare the benefits and premiums of the individual insurers beforehand.
    </div>
  </div>

  <!-- Driving: dark band -->
  <div class="abs" style="left:0;top:1710px;width:503px;height:420px;background:var(--navy)"></div>
  <svg class="abs" style="left:0;top:2085px" width="503" height="75" viewBox="0 0 503 75">
    <rect x="0" y="0" width="503" height="75" fill="#e3e7eb"/>
    <polygon points="0,0 503,0 503,68 0,15" fill="#0a2b46"/>
    <polygon points="0,18 200,38 0,68" fill="#8595a4"/>
  </svg>
  <div class="abs frame on-dark" style="left:60px;top:1740px;width:184px;height:355px"></div>
  <div class="abs" role="img" aria-label="Motorway winding through a landscape at dusk" style="left:67px;top:1747px;width:177px;height:348px;background:linear-gradient(180deg,#e3c9c0 0%,#a8b3bf 30%,#6c7e8e 60%,#3c4a57 100%)"></div>
  <div class="abs card dark" style="left:185px;top:1767px;width:268px;height:304px;background:#0c3050">
    <h3 class="abs" style="left:14px;top:17px;font-weight:400">Driving <b>in Switzerland</b></h3>
    <div class="acc boxed" style="left:14px;top:36px;width:236px">General information about driving in Switzerland</div>
    <div class="acc white" style="left:14px;top:56px;width:236px">Currency and banking</div>
    <div class="small abs light" style="left:20px;top:77px;width:226px">
      A valid driver's license is required to drive a vehicle. Foreigners may drive in Switzerland for up to one year with a driver's license from their home country or an international driver's license. After that, a Swiss driver's license must be applied for at the traffic licensing authority. Necessary for this are:
      <ul><li>Completing the application to exchange the foreign driver's license for a Swiss driver's license</li><li>Enclose the previous driver's license (will then be stamped as "invalid in Switzerland")</li><li>Proof of a vision test by an ophthalmologist confirming perfect eyesight</li><li>Passport photo</li><li>Foreigner's identity card (B or C identity card) as confirmation of residence</li></ul>
    </div>
    <div class="acc dark-line" style="left:14px;top:191px;width:236px">Have vehicle safety checked</div>
    <div class="acc dark-line" style="left:14px;top:211px;width:236px">Buy vehicle</div>
    <div class="acc dark-line" style="left:14px;top:231px;width:236px">Import vehicle</div>
    <div class="acc dark-line" style="left:14px;top:251px;width:236px">Insure vehicle</div>
  </div>

  <!-- Public transport -->
  <div class="abs" style="left:0;top:2160px;width:503px;height:238px;background:#fff"></div>
  <div class="abs frame" style="left:261px;top:2158px;width:181px;height:197px"></div>
  <div class="abs" role="img" aria-label="Airport terminal with an aircraft under a cloudy sky" style="left:256px;top:2163px;width:180px;height:201px;background:linear-gradient(180deg,#9eb4c9 0%,#5b7894 45%,#2e4a66 100%)"></div>
  <div class="abs card" style="left:54px;top:2183px;width:264px;height:170px">
    <h3 class="abs" style="left:13px;top:18px;font-weight:400">Public <b>transport in Switzerland</b></h3>
    <div class="acc" style="left:13px;top:36px;width:236px">Bus and train</div>
    <div class="acc open" style="left:13px;top:56px;width:236px">Air traffic</div>
    <div class="small abs" style="left:19px;top:78px;width:226px">
      Internationally, Switzerland is also very easy to reach from any corner of the world with three national airports. The three airports are located in <a>Zurich, Geneva and Basel-Mulhouse</a> (which is geographically located in France near the Swiss border).<br>
      From Zurich and Geneva, destinations within and outside Europe are served, and from Basel-Mulhouse, destinations within Europe.<br>
      In addition to these three major international hubs, there are also eleven regional airports, from which various destinations in Europe are served.
    </div>
  </div>

  <!-- Footer -->
  <div class="abs footer" style="left:0;top:2398px;width:503px;height:140px">
    <div class="abs" style="left:67px;top:33px;display:flex;align-items:center;gap:5px;color:#fff">
      <span style="width:18px;height:18px;border-radius:50%;background:#fff;display:block"></span>
      <span style="font-size:8px;font-weight:600;line-height:9px;text-transform:uppercase;letter-spacing:.03em">Fiscorana<br>Advisory</span>
    </div>
    <div class="abs tiny" style="left:67px;top:62px">
      <div style="display:flex;align-items:center;gap:3px"><svg width="5" height="6" viewBox="0 0 10 12"><path d="M5 0a4 4 0 0 0-4 4c0 3 4 8 4 8s4-5 4-8a4 4 0 0 0-4-4z" fill="#fff"/></svg>Office Lenzbach, Lindenweg 12</div>
      <div style="display:flex;align-items:center;gap:3px"><svg width="5" height="6" viewBox="0 0 10 10"><path d="M2 0l2 2-1 2c1 2 2 3 4 4l2-1 2 2-2 2C4 10 0 6 0 2z" fill="#fff"/></svg>Available for existing clients only</div>
      <div style="display:flex;align-items:center;gap:3px"><svg width="6" height="5" viewBox="0 0 12 9"><rect width="12" height="9" fill="#fff"/><path d="M0 0l6 5 6-5" stroke="#0a2b46" fill="none"/></svg>Available for existing clients only</div>
    </div>
    <div class="abs col-title" style="left:192px;top:33px">About Fiscorana</div>
    <div class="abs tiny" style="left:192px;top:46px;width:120px">Fiscorana Advisory was founded in 2014 with the vision to make life for expats in Switzerland easier and to handle their tax matters efficiently, digitally and with care.</div>
    <div class="abs col-title" style="left:349px;top:33px">Quick links</div>
    <div class="abs tiny" style="left:349px;top:46px">Tax returns<br>Pricing<br>Swiss tax guide<br>About us<br>Privacy policy</div>
    <div class="abs" style="left:0;top:118px;width:503px;height:1px;background:#2d4b66"></div>
    <div class="abs tiny" style="left:0;top:124px;width:503px;text-align:center">2022 Fiscorana Advisory LLC All Right Reserved | Privacy Policy | Imprint</div>
  </div>
</div>

</body>
</html>
```